dessert restaurant

I need a business card design for my restaurant. It will primarily be a dessert and wine restaurant. I will serve delicious baked from scratch desserts, cake, pies cookies brownies etc. Select red and white wines.I will also offer light breakfast, and lunch menu. This will be an upscale contemporary design restaurant with reasonably priced items on the menu. I will also offer small plates in the evening with dessert menu. my color scheme is cobalt blue , red, white black. My restaurant will be the place where adults come after enjoying the meal at a restaurant and want to enjoy a dessert and a glass of wine to finish off their evening. I will also have contemporary jazz sounds for atmosphere.

Industry/Entity Type

Restaurant

Contact Information for Business Card

delia marsh 415 862 3094

```html
<!DOCTYPE html>
<html lang="en">
<head>
<meta charset="utf-8">
<title>Indulgence – Dessert and Wine Restaurant</title>
<link rel="stylesheet" href="https://fonts.googleapis.com/css2?family=Almendra:wght@700&family=Cinzel:wght@400&family=Tinos&family=Italianno&family=Arimo&display=swap">
<style>
  :root {
    --ink: #111111;
    --red: #e0161b;
    --cobalt: #1f3ff0;
    --white: #ffffff;
    --wine: #5a0e12;
    --glass: #e9e9ea;
    --cream: #efe6d8;
    --cocoa: #6b3f22;
  }
  html, body { margin: 0; padding: 0; overflow: hidden; background: var(--white); }
  .card {
    position: relative;
    width: 1200px;
    height: 702px;
    overflow: hidden;
    background: var(--white);
    color: var(--ink);
    font-family: "Tinos", "Times New Roman", serif;
  }
  .brand-name {
    position: absolute;
    left: 0; width: 1200px; top: 30px;
    margin: 0;
    text-align: center;
    font-family: "Almendra", serif;
    font-weight: 700;
    font-size: 128px;
    line-height: 1;
    color: var(--ink);
    letter-spacing: 2px;
  }
  .tagline {
    position: absolute;
    left: 60px; top: 180px;
    margin: 0;
    font-family: "Cinzel", serif;
    font-size: 35px;
    letter-spacing: 2px;
    color: var(--red);
    white-space: nowrap;
  }
  .offer-box {
    position: absolute;
    left: 89px; top: 227px;
    width: 842px; height: 100px;
    box-sizing: border-box;
    background: var(--cobalt);
    border-radius: 18px;
    box-shadow: -8px 6px 0 var(--ink);
    display: flex; align-items: center; justify-content: center;
    text-align: center;
    color: var(--white);
    font-size: 31px;
    line-height: 41px;
  }
  .offer-box p { margin: 0; }
  .mission {
    position: absolute;
    left: 40px; width: 640px; top: 352px;
    margin: 0;
    text-align: center;
    font-size: 21px;
    line-height: 28px;
  }
  .owner-name {
    position: absolute;
    left: 40px; width: 640px; top: 444px;
    margin: 0;
    text-align: center;
    font-family: "Italianno", cursive;
    font-size: 72px;
    line-height: 1;
    color: var(--red);
  }
  .owner-phone {
    position: absolute;
    left: 40px; width: 640px; top: 522px;
    margin: 0;
    text-align: center;
    font-family: "Arimo", Arial, sans-serif;
    font-size: 44px;
    line-height: 1;
    color: var(--red);
  }
  .address, .hours {
    position: absolute;
    left: 50px;
    margin: 0;
    font-size: 22px;
    white-space: nowrap;
  }
  .address { top: 587px; }
  .hours { top: 626px; }
  .wine-photo {
    position: absolute;
    left: 995px; top: 174px;
    width: 155px; height: 345px;
    border-radius: 70px 70px 40px 40px / 120px 120px 20px 20px;
    background: linear-gradient(180deg, var(--glass) 0%, var(--wine) 22%, #2a0608 48%, var(--glass) 62%, #f6f6f6 100%);
  }
  .dessert-photo {
    position: absolute;
    left: 645px; top: 368px;
    width: 350px; height: 250px;
    border-radius: 30px;
    background: radial-gradient(ellipse at 45% 40%, var(--cocoa) 0%, #a98a6a 30%, var(--cream) 55%, #f4f4f4 80%);
  }
</style>
</head>
<body>
<main class="card">
  <h1 class="brand-name">Indulgence</h1>
  <p class="tagline">Dessert and wine restaurant</p>

  <div class="offer-box">
    <p>We serve delicious baked from scratch desserts, cake,<br>pies, cookies, brownies etc. Select red and white wines.</p>
  </div>

  <p class="mission">A place where you can come after enjoying your meal<br>at a restaurant and want to enjoy a dessert and a<br>glass of wine to finish off your evening.</p>

  <p class="owner-name">Delia Marsh</p>
  <p class="owner-phone">415 862 3094</p>

  <p class="address">1187 Marlow Ave, N.W. Wash D.C. 20012</p>
  <p class="hours">Breakfast &amp; Lunch / Mon-Sat 8a-2p Closed on sunday all day.&nbsp; Evening hours / Thurs-Sat 4p-10p</p>

  <div class="wine-photo" role="img" aria-label="Photo of a glass of red wine"></div>
  <div class="dessert-photo" role="img" aria-label="Photo of a slice of tiramisu on a white plate with a fork"></div>
</main>
</body>
</html>
```